Package design for Mica powder sachets

Our mica powder product comes in two sets of colors, a set of 60 and 35 packed inside sachet bags individually. This project will require two sizes of the packing box , one for the set of 60 and other for 35. We do not have a specific design requirement as long as the design reflects the theme of our product. Box diagram for both sizes is attached together with color chart, content, logo, sachet design and sample of a packaging design we like. The content is the same for both sizes accept for number of colors included.

```html
<!DOCTYPE html>
<html lang="en">
<head>
<meta charset="utf-8">
<title>Lumenwell – Mica Powder Box Dieline</title>
<link rel="stylesheet" href="https://fonts.googleapis.com/css2?family=Roboto:wght@500;700;900&display=swap">
<style>
  :root{
    --page:#ffffff;
    --board:#ffffff;
    --board-edge:#d9d9d9;
    --navy:#15173f;
    --orange:#f2942a;
    --bullet:#f5d31c;
    --ink:#222222;
  }
  *{margin:0;padding:0;box-sizing:border-box}
  html,body{width:1200px;height:1200px;overflow:hidden;background:var(--page)}
  .canvas{position:relative;width:1200px;height:1200px}
  .dieline{position:absolute;left:0;top:0}
  .dieline .flap{fill:var(--board);stroke:var(--board-edge);stroke-width:1}

  .colour-chart{
    position:absolute;left:258px;top:350px;width:180px;
    display:flex;gap:14px;
    font-family:"Roboto",sans-serif;font-weight:700;font-size:4.8px;line-height:6.35px;color:var(--ink);
  }
  .colour-chart ul{list-style:none;width:86px}
  .colour-chart li{white-space:nowrap;height:6.35px}
  .colour-chart li::before{
    content:"";display:inline-block;width:3px;height:3px;border-radius:50%;
    background:var(--bullet);margin-right:4px;vertical-align:middle
  }
  .colour-chart li.gap::before{display:none}
  .colour-chart .code{display:inline-block;width:14px}

  .brand{
    position:absolute;font-family:"Roboto",sans-serif;font-weight:700;color:var(--navy);
    text-align:center;line-height:1;letter-spacing:0;
  }
  .brand--back{left:243px;width:197px;top:722px;font-size:32px}
  .brand--front{left:707px;width:266px;top:548px;font-size:40px}

  .product-line{
    position:absolute;left:707px;width:266px;text-align:center;
    font-family:"Roboto",sans-serif;color:var(--orange);line-height:1;
  }
  .product-line--count{top:615px;font-size:15px;font-weight:900}
  .product-line--name{top:634px;font-size:23px;font-weight:700}
</style>
</head>
<body>
<div class="canvas">
  <svg class="dieline" width="1200" height="1200" viewBox="0 0 1200 1200" xmlns="http://www.w3.org/2000/svg">
    <defs>
      <linearGradient id="artwork-left" x1="0" y1="0" x2="1" y2="1">
        <stop offset="0" stop-color="#ffffff"/>
        <stop offset="0.3" stop-color="#9fdde6"/>
        <stop offset="0.6" stop-color="#8cc63e"/>
        <stop offset="0.85" stop-color="#2a74d6"/>
        <stop offset="1" stop-color="#f2942a"/>
      </linearGradient>
      <linearGradient id="artwork-right" x1="0" y1="0" x2="1" y2="1">
        <stop offset="0" stop-color="#8cc63e"/>
        <stop offset="0.3" stop-color="#2a74d6"/>
        <stop offset="0.55" stop-color="#34c0ea"/>
        <stop offset="0.8" stop-color="#5fb24a"/>
        <stop offset="1" stop-color="#f2942a"/>
      </linearGradient>
      <filter id="board-shadow" x="-5%" y="-5%" width="110%" height="110%">
        <feDropShadow dx="0" dy="1" stdDeviation="2" flood-color="#000" flood-opacity="0.18"/>
      </filter>
    </defs>

    <g filter="url(#board-shadow)">
      <rect class="flap" x="36" y="160" width="121" height="174"/>
      <rect class="flap" x="160" y="160" width="384" height="174"/>
      <rect class="flap" x="547" y="160" width="120" height="174"/>
      <path class="flap" d="M667 334 L667 240 Q667 195 700 180 Q725 160 760 160 L960 160 Q1000 160 1010 180 Q1043 195 1043 240 L1043 334 Z"/>
      <rect class="flap" x="36" y="826" width="121" height="137"/>
      <rect class="flap" x="160" y="826" width="384" height="137"/>
      <rect class="flap" x="547" y="826" width="120" height="137"/>
      <path class="flap" d="M667 800 L667 880 Q667 925 700 940 Q725 963 760 963 L960 963 Q1000 963 1010 940 Q1043 925 1043 880 L1043 800 Z"/>
      <path class="flap" d="M1043 160 L1160 160 L1184 185 L1184 938 L1160 963 L1043 963 Z"/>
      <rect class="flap" x="36" y="333" width="1007" height="467"/>
    </g>

    <rect x="36" y="333" width="207" height="467" fill="url(#artwork-left)" role="img" aria-label="Abstract brush strokes and dotted shapes in blue, green and orange"/>
    <rect x="440" y="333" width="603" height="467" fill="url(#artwork-right)" role="img" aria-label="Abstract brush strokes and dotted shapes in blue, green and orange"/>

    <circle cx="840" cy="567" r="133" fill="#ffffff"/>
    <circle cx="840" cy="567" r="142" fill="none" stroke="#ffffff" stroke-width="3" opacity="0.8"/>
  </svg>

  <div class="colour-chart">
    <ul>
      <li><span class="code">M1</span>WINDY BLUE</li>
      <li><span class="code">M2</span>SAGE GLOW</li>
      <li><span class="code">M4</span>PEACH BLOSSOM</li>
      <li class="gap"></li>
      <li><span class="code">M5</span>GOLD GLOW</li>
      <li><span class="code">M6</span>PEARL WHITE</li>
      <li><span class="code">M7</span>LIGHT GOLD</li>
      <li class="gap"></li>
      <li><span class="code">M9</span>YELLOW GOLD</li>
      <li class="gap"></li>
      <li class="gap"></li>
      <li><span class="code">M12</span>CLASSIC GOLD</li>
      <li><span class="code">M13</span>GLITZY GOLD</li>
      <li class="gap"></li>
      <li><span class="code">M15</span>TUSCANY YELLOW</li>
      <li><span class="code">M16</span>CITRUS ZEST</li>
      <li class="gap"></li>
      <li><span class="code">M18</span>LEMON TWIST</li>
      <li class="gap"></li>
      <li><span class="code">M20</span>RAVEN GRAY</li>
      <li><span class="code">M21</span>CHARCOAL</li>
      <li><span class="code">M22</span>SPACE GRAY</li>
      <li><span class="code">M23</span>CHOCOLATE BROWN</li>
      <li><span class="code">M24</span>BRONZE</li>
      <li class="gap"></li>
      <li><span class="code">M26</span>MOCHA BROWN</li>
      <li><span class="code">M27</span>GOLDEN BROWN</li>
      <li class="gap"></li>
      <li><span class="code">M29</span>JUNGLE GREEN</li>
      <li><span class="code">M30</span>SEA GREEN</li>
      <li><span class="code">M31</span>TURQUOISE</li>
      <li><span class="code">M32</span>MINT GREEN</li>
      <li class="gap"></li>
      <li><span class="code">M34</span>HUNTER GREEN</li>
      <li><span class="code">M35</span>EMERALD GREEN</li>
      <li><span class="code">M36</span>SPRING GREEN</li>
      <li class="gap"></li>
      <li><span class="code">M39</span>FOREST GREEN</li>
      <li class="gap"></li>
      <li><span class="code">M40</span>SKY BLUE</li>
    </ul>
    <ul>
      <li><span class="code">M42</span>MARLIN BLUE</li>
      <li><span class="code">M43</span>DENIM BLUE</li>
      <li><span class="code">M44</span>WHALE BLUE</li>
      <li><span class="code">M45</span>BRIGHT BLUE</li>
      <li class="gap"></li>
      <li><span class="code">M47</span>SAPPHIRE BLUE</li>
      <li><span class="code">M48</span>OCEAN BLUE</li>
      <li><span class="code">M49</span>NAVY BLUE</li>
      <li><span class="code">M50</span>ROYAL PURPLE</li>
      <li class="gap"></li>
      <li class="gap"></li>
      <li><span class="code">M53</span>VIOLET PURPLE</li>
      <li><span class="code">M54</span>IRIS</li>
      <li><span class="code">M55</span>LAVENDER</li>
      <li><span class="code">M56</span>DUSK PURPLE</li>
      <li><span class="code">M57</span>CORAL ORANGE</li>
      <li><span class="code">M58</span>NEON ORANGE</li>
      <li><span class="code">M59</span>ROSE RED</li>
      <li><span class="code">M60</span>CRIMSON RED</li>
      <li><span class="code">M61</span>RUBY</li>
      <li><span class="code">M62</span>RASPBERRY</li>
      <li class="gap"></li>
      <li class="gap"></li>
      <li><span class="code">M65</span>MAGENTA</li>
      <li class="gap"></li>
      <li><span class="code">M67</span>ROSE PINK</li>
      <li><span class="code">M68</span>MAHOGANY</li>
      <li><span class="code">M69</span>MAROON</li>
      <li><span class="code">M70</span>HOT PINK</li>
      <li class="gap"></li>
      <li><span class="code">M72</span>LILAC</li>
      <li><span class="code">M73</span>CREAMY PINK</li>
      <li><span class="code">M74</span>BURGUNDY</li>
      <li><span class="code">M75</span>COPPER</li>
      <li><span class="code">M76</span>BRONZE GOLD</li>
      <li><span class="code">M77</span>BURNT ORANGE</li>
      <li><span class="code">M78</span>BRILLIANT SILVER</li>
      <li><span class="code">M79</span>PEWTER</li>
      <li><span class="code">M80</span>OLIVE GREEN</li>
    </ul>
  </div>

  <div class="brand brand--back">Lumenwell</div>

  <div class="brand brand--front">Lumenwell</div>
  <div class="product-line product-line--count">60 INSPIRING</div>
  <div class="product-line product-line--name">MICA POWDER</div>
</div>
</body>
</html>
```